Torretta Gelato Pints

6 flavors , pints italian , southern , organic , natural feel

Pistachio , chocolate, strawberry , hazelnut , vaniglia

Stracciiatelle

Target Market(s)

Upscale

Requirements
Must have
• See graphic upload . Want that look.. showing freshbest quality in gradients of each flavor

```html
<!DOCTYPE html>
<html lang="en">
<head>
<meta charset="utf-8">
<title>Torretta Gelato – Pint Label Directions</title>
<link href="https://fonts.googleapis.com/css2?family=Dosis:wght@400;500&display=swap" rel="stylesheet">
<style>
  :root{
    --bg:#5f5f5f;
    --paper:#ffffff;
    --red:#e8192c;
    --brown:#4e2a1e;
    --pink:#f28ea0;
    --teal:#52c2b6;
    --green:#3aaa48;
    --label-ink:#3d3d3d;
  }
  *{box-sizing:border-box;margin:0;padding:0}
  html,body{width:958px;height:1200px;overflow:hidden}
  body{background:var(--bg);font-family:"Dosis",sans-serif;position:relative;color:#fff}

  .sheet-title{position:absolute;left:0;width:926px;text-align:center;font-size:24px;letter-spacing:2px;line-height:1}
  .sheet-title.t1{top:34px}
  .sheet-title.t2{top:66px}

  .scheme-title{position:absolute;top:126px;width:200px;text-align:center;font-size:24px;letter-spacing:2.5px;line-height:1}

  .swatch{position:absolute;top:185px;width:59px;height:76px;background:var(--paper);padding:3px}
  .swatch .chip{height:53px}
  .swatch .code{font-size:7px;color:var(--label-ink);text-align:center;line-height:16px;letter-spacing:.1px;white-space:nowrap}

  .lid{position:absolute;top:310px;width:218px;height:218px;border-radius:50%;background:var(--paper)}
  .lid .ring{position:absolute;inset:10px;border:1px solid var(--brown);border-radius:50%}
  .lid .brand{position:absolute;top:72px;left:0;right:0;text-align:center;font-size:34px;letter-spacing:3px;line-height:1}
  .lid .rule{position:absolute;top:112px;left:40px;right:40px;height:1px}
  .lid .tagline{position:absolute;top:132px;left:0;right:0;text-align:center;font-size:14px;line-height:1}

  .pint{position:absolute;width:211px;height:235px;background:var(--paper)}
  .pint .brand{position:absolute;top:17px;left:0;right:0;text-align:center;font-size:26px;letter-spacing:2.5px;line-height:1}
  .pint .rule{position:absolute;top:51px;left:48px;right:48px;height:1px}
  .pint .tagline{position:absolute;top:62px;left:0;right:0;text-align:center;font-size:11px;line-height:1}
  .pint .art{position:absolute;top:78px;left:45px;width:121px;height:92px;border-radius:46%}
  .pint .flavor-band{position:absolute;top:183px;left:53px;width:106px;height:14px;border-radius:7px}
  .pint .flavor{position:absolute;top:185px;left:0;right:0;text-align:center;font-size:10px;letter-spacing:1.2px;color:var(--label-ink);line-height:1}
  .pint .volume{position:absolute;top:215px;left:89px;width:34px;height:19px;font-size:7.5px;color:#fff;text-align:center;line-height:19px}

  .scheme-a .brand,.scheme-c .brand{color:var(--red)}
  .scheme-a .rule,.scheme-c .rule{background:var(--red)}
  .scheme-a .tagline{color:var(--brown)}
  .scheme-b .brand{color:var(--pink)}
  .scheme-b .rule{background:var(--pink)}
  .scheme-b .tagline{color:var(--teal)}
  .scheme-c .tagline{color:var(--green)}
  .scheme-a .volume,.scheme-c .volume{background:var(--brown)}
  .scheme-b .volume{background:var(--teal)}
</style>
</head>
<body>

  <div class="sheet-title t1">CONTOURS</div>
  <div class="sheet-title t2">FONT: DOSIS REGULAR</div>

  <div class="scheme-title" style="left:71px">COLORS A</div>
  <div class="scheme-title" style="left:363px">COLORS B</div>
  <div class="scheme-title" style="left:658px">COLORS C</div>

  <!-- Palette A -->
  <div class="swatch" style="left:113px"><div class="chip" style="background:var(--red)"></div><div class="code">CHROMA 185C</div></div>
  <div class="swatch" style="left:179px"><div class="chip" style="background:var(--brown)"></div><div class="code">CHROMA 4625C</div></div>
  <!-- Palette B -->
  <div class="swatch" style="left:360px"><div class="chip" style="background:var(--pink)"></div><div class="code">CHROMA 1775C</div></div>
  <div class="swatch" style="left:432px"><div class="chip" style="background:var(--brown)"></div><div class="code">CHROMA 4625C</div></div>
  <div class="swatch" style="left:502px"><div class="chip" style="background:var(--teal)"></div><div class="code">CHROMA 333C</div></div>
  <!-- Palette C -->
  <div class="swatch" style="left:663px"><div class="chip" style="background:var(--red)"></div><div class="code">CHROMA 185C</div></div>
  <div class="swatch" style="left:728px"><div class="chip" style="background:var(--brown)"></div><div class="code">CHROMA 4625C</div></div>
  <div class="swatch" style="left:793px"><div class="chip" style="background:var(--green)"></div><div class="code">CHROMA 361C</div></div>

  <!-- Lids -->
  <div class="lid scheme-a" style="left:66px"><div class="ring"></div><div class="brand">TORRETTA</div><div class="rule"></div><div class="tagline">ITALIAN GELATO</div></div>
  <div class="lid scheme-b" style="left:354px"><div class="ring"></div><div class="brand">TORRETTA</div><div class="rule"></div><div class="tagline">ITALIAN GELATO</div></div>
  <div class="lid scheme-c" style="left:641px"><div class="ring"></div><div class="brand">TORRETTA</div><div class="rule"></div><div class="tagline">ITALIAN GELATO</div></div>

  <!-- Pints row 1 -->
  <div class="pint scheme-a" style="left:68px;top:552px">
    <div class="brand">TORRETTA</div><div class="rule"></div><div class="tagline">ITALIAN GELATO</div>
    <div class="art" role="img" aria-label="Painted pistachio nuts in their shells" style="background:radial-gradient(circle at 50% 55%,#c8d98a 0%,#d9a67c 45%,rgba(255,255,255,0) 72%)"></div>
    <div class="flavor-band" style="background:linear-gradient(90deg,rgba(200,225,180,.2),#dcebcf 30%,#e3efd7 70%,rgba(200,225,180,.2))"></div>
    <div class="flavor">PISTACHIO</div>
    <div class="volume">473ML</div>
  </div>
  <div class="pint scheme-b" style="left:356px;top:552px">
    <div class="brand">TORRETTA</div><div class="rule"></div><div class="tagline">ITALIAN GELATO</div>
    <div class="art" role="img" aria-label="Painted chocolate pieces and cocoa beans" style="background:radial-gradient(circle at 50% 55%,#4a1f17 0%,#6e3528 45%,rgba(255,255,255,0) 72%)"></div>
    <div class="flavor-band" style="background:linear-gradient(90deg,rgba(225,220,212,.2),#e8e3dc 30%,#ebe6df 70%,rgba(225,220,212,.2))"></div>
    <div class="flavor">CHOCOLATE</div>
    <div class="volume">473ML</div>
  </div>
  <div class="pint scheme-c" style="left:643px;top:552px">
    <div class="brand">TORRETTA</div><div class="rule"></div><div class="tagline">ITALIAN GELATO</div>
    <div class="art" role="img" aria-label="Painted ripe strawberries with green leaves" style="background:radial-gradient(circle at 50% 55%,#e0252c 0%,#e85050 45%,rgba(255,255,255,0) 72%)"></div>
    <div class="flavor-band" style="background:linear-gradient(90deg,rgba(245,200,205,.2),#f8d0d5 30%,#f9d6da 70%,rgba(245,200,205,.2))"></div>
    <div class="flavor">STRAWBERRY</div>
    <div class="volume">473ML</div>
  </div>

  <!-- Pints row 2 -->
  <div class="pint scheme-a" style="left:67px;top:819px">
    <div class="brand">TORRETTA</div><div class="rule"></div><div class="tagline">ITALIAN GELATO</div>
    <div class="art" role="img" aria-label="Painted hazelnuts with a leaf" style="background:radial-gradient(circle at 50% 55%,#f2c27a 0%,#9a4f24 45%,rgba(255,255,255,0) 72%)"></div>
    <div class="flavor-band" style="background:linear-gradient(90deg,rgba(245,228,210,.2),#f6e7d8 30%,#f8ebde 70%,rgba(245,228,210,.2))"></div>
    <div class="flavor">HAZELNUT</div>
    <div class="volume">473ML</div>
  </div>
  <div class="pint scheme-b" style="left:355px;top:819px">
    <div class="brand">TORRETTA</div><div class="rule"></div><div class="tagline">ITALIAN GELATO</div>
    <div class="art" role="img" aria-label="Painted vanilla flower with vanilla pods" style="background:radial-gradient(circle at 50% 55%,#f5e04a 0%,#e8e6b8 45%,rgba(255,255,255,0) 72%)"></div>
    <div class="flavor-band" style="background:linear-gradient(90deg,rgba(250,240,180,.2),#faf2bf 30%,#fbf4c8 70%,rgba(250,240,180,.2))"></div>
    <div class="flavor">VANIGLIA</div>
    <div class="volume">473ML</div>
  </div>
  <div class="pint scheme-c" style="left:643px;top:819px">
    <div class="brand">TORRETTA</div><div class="rule"></div><div class="tagline">ITALIAN GELATO</div>
    <div class="art" role="img" aria-label="Painted scoop of stracciatella cream" style="background:radial-gradient(circle at 50% 55%,#ebe8e2 0%,#f2f0ec 45%,rgba(255,255,255,0) 72%)"></div>
    <div class="flavor">STRACCIATELLA</div>
    <div class="volume">473ML</div>
  </div>

</body>
</html>
```